Book cover for book of Poems "Lanternfall"

I have written a book of poems. The book is titled "Lanternfall" and has 160 pages. The poems were written mostly during my youth but there are newer poems also written over the past 10 years (I'm 42 now). They are mostly about love, loss, social conformity, and nature. I'm influenced a lot by the English Romantic Poets, gothic motives, and 80s music by bands such as The Vell, Porvana & the Quillets, and Tabberley. I need an original book cover design for my book. Attached are samples of designs I like and few of my poems. The cover will be a hardcover and I need design for Front Cover, Back Cover, and Spine. Dimension is 6"x9". Front Cover should have name of book "Lanternfall" and name of author "Ravi Dunsker". Thanks.
Updates

Further details which I should have included in my original brief -The book cover will be a hard cover. Design is required for front cover, back cover, and spine. Dimension is 6x9.Front should have book title "Lanternfall" and author's name "Ravi Dunsker". Added Monday, December 19, 2016

Target Market(s)

Mostly friends and family

Requirements
Must have
• I don't mind a design where lanternfall is spelled out in big capital letters and text from one of my poems is inside, like the sample I've attached.

```html
<!DOCTYPE html>
<html lang="en">
<head>
<meta charset="utf-8">
<title>Lanternfall — Cover Spread</title>
<link rel="stylesheet" href="https://fonts.googleapis.com/css2?family=EB+Garamond:ital,wght@0,400;1,400&family=Petit+Formal+Script&display=swap">
<style>
  :root {
    --board: #000000;
    --gutter: #ffffff;
    --ink-light: #f2f2f2;
    --title-slate: #4b5866;
    --script: #dcdcdc;
    --placeholder-grey: #dcdcdd;
    --frame-gold: #b8962e;
  }
  html, body {
    margin: 0;
    padding: 0;
    width: 1200px;
    height: 814px;
    overflow: hidden;
    background: var(--gutter);
  }
  .spread {
    position: relative;
    width: 1200px;
    height: 814px;
    background: var(--gutter);
    font-family: "EB Garamond", Georgia, serif;
  }
  .panel {
    position: absolute;
    top: 0;
    height: 813px;
    background: var(--board);
    overflow: hidden;
  }
  .back-cover { left: 0; width: 542px; }
  .spine { left: 552px; width: 98px; }
  .front-cover { left: 659px; width: 541px; }

  .back-cover__image-slot {
    position: absolute;
    left: 42px;
    top: 446px;
    width: 161px;
    height: 161px;
    background: var(--placeholder-grey);
  }
  .imprint {
    position: absolute;
    width: 58px;
    height: 58px;
    border: 2px solid var(--frame-gold);
    display: flex;
    align-items: center;
    justify-content: center;
    text-align: center;
    color: var(--ink-light);
    font-size: 6.5px;
    line-height: 1.15;
    letter-spacing: 0.02em;
  }
  .back-cover .imprint { left: 42px; top: 720px; }
  .spine .imprint { left: 17px; top: 696px; }

  .spine__author {
    position: absolute;
    left: 50%;
    top: 106px;
    transform: translate(-50%, -50%) rotate(-90deg);
    color: var(--ink-light);
    font-size: 24px;
    line-height: 26px;
    letter-spacing: 0.12em;
    text-align: left;
    white-space: nowrap;
  }
  .spine__title {
    position: absolute;
    left: 50%;
    top: 406px;
    transform: translate(-50%, -50%) rotate(-90deg);
    color: var(--title-slate);
    font-style: italic;
    font-size: 62px;
    line-height: 1;
    white-space: nowrap;
  }

  .front-cover__author {
    position: absolute;
    top: 48px;
    left: 0;
    width: 541px;
    text-align: center;
    color: var(--ink-light);
    font-size: 21px;
    letter-spacing: 0.32em;
    padding-left: 0.32em;
    box-sizing: border-box;
  }
  .poem {
    position: absolute;
    top: 0;
    left: 0;
    width: 541px;
    margin: 0;
    padding: 0;
    list-style: none;
    text-align: center;
    font-family: "Petit Formal Script", cursive;
    color: var(--script);
  }
  .poem__line {
    position: absolute;
    left: 0;
    width: 541px;
    font-size: 14px;
    line-height: 16px;
    white-space: nowrap;
    -webkit-mask-image: linear-gradient(90deg, transparent 26%, #000 40%, #000 60%, transparent 74%);
            mask-image: linear-gradient(90deg, transparent 26%, #000 40%, #000 60%, transparent 74%);
  }
  .poem__line--faint { opacity: 0.3; }
  .poem__line--dim { opacity: 0.55; }
  .poem__line--soft { opacity: 0.75; }
  .poem__line--clear { opacity: 0.95; }

  .front-cover__title {
    position: absolute;
    top: 560px;
    left: 0;
    width: 541px;
    margin: 0;
    text-align: center;
    color: var(--title-slate);
    font-style: italic;
    font-weight: 400;
    font-size: 88px;
    line-height: 1;
    white-space: nowrap;
  }
</style>
</head>
<body>
<main class="spread">
  <section class="panel back-cover" aria-label="Back cover">
    <div class="back-cover__image-slot" role="img" aria-label="Reserved area for back cover image"></div>
    <div class="imprint">LOGO<br>PLACEHOLDER</div>
  </section>

  <section class="panel spine" aria-label="Spine">
    <div class="spine__author">RAVI<br>DUNSKER</div>
    <div class="spine__title">Lanternfall</div>
    <div class="imprint">LOGO<br>PLACEHOLDER</div>
  </section>

  <section class="panel front-cover" aria-label="Front cover">
    <div class="front-cover__author">RAVI DUNSKER</div>
    <ul class="poem">
      <li class="poem__line poem__line--faint" style="top:289px">We've drifted into dusk and flame</li>
      <li class="poem__line poem__line--dim" style="top:318px">Our hearts forgot their name</li>
      <li class="poem__line poem__line--dim" style="top:346px">We've drifted into dusk and flame</li>
      <li class="poem__line poem__line--soft" style="top:375px">Our vow grew cold the hour it came</li>
      <li class="poem__line poem__line--clear" style="top:432px">Where did the lantern go</li>
      <li class="poem__line poem__line--clear" style="top:461px">Why did we dim its glow</li>
      <li class="poem__line poem__line--soft" style="top:490px">We swore the light would stay</li>
      <li class="poem__line poem__line--soft" style="top:518px">How did it slip away</li>
      <li class="poem__line poem__line--faint" style="top:575px">We've drifted into ash and rain</li>
      <li class="poem__line poem__line--faint" style="top:604px">We fell again</li>
    </ul>
    <h1 class="front-cover__title">Lanternfall</h1>
  </section>
</main>
</body>
</html>
```